Flyer Design Project

4x3 wall sticker with IN CASE OF EMERGENCY OR FOR ACCESS, CONTACT OUR LOGO AND PHONE NUMBER I CAN SEND YOU THE LOGO AND A SAMPLE PICTURE IF NEED BE

```html
<!DOCTYPE html>
<html lang="en">
<head>
<meta charset="utf-8">
<title>Emergency Access Wall Sticker</title>
<link href="https://fonts.googleapis.com/css2?family=Montserrat:wght@400;500;600&display=swap" rel="stylesheet">
<style>
  :root {
    --navy: #0d3f69;
    --sky: #0a82c3;
    --paper: #ffffff;
    --ink-light: #f2f2f2;
    --edge: #e4e4e4;
  }
  * { margin: 0; padding: 0; box-sizing: border-box; }
  html, body {
    width: 1200px;
    height: 901px;
    overflow: hidden;
    background: var(--paper);
  }
  .sticker {
    position: relative;
    width: 1200px;
    height: 901px;
    background: var(--paper);
    border: 2px solid var(--edge);
    font-family: "Montserrat", sans-serif;
  }
  .header-shape {
    position: absolute;
    left: 0;
    top: 0;
    width: 1200px;
    height: 901px;
  }
  .headline {
    position: absolute;
    left: 116px;
    top: 138px;
    color: var(--ink-light);
    font-weight: 400;
    font-size: 86px;
    line-height: 98px;
    letter-spacing: 2px;
    text-transform: uppercase;
  }
  .contact-box {
    position: absolute;
    left: 60px;
    top: 588px;
    width: 1080px;
    height: 254px;
    border: 3px solid var(--navy);
    border-top: none;
  }
  .brand {
    position: absolute;
    left: 105px;
    top: 650px;
    display: flex;
    align-items: center;
    gap: 28px;
  }
  .brand-square {
    width: 96px;
    height: 96px;
    background: var(--sky);
  }
  .brand-name {
    color: var(--navy);
    font-weight: 400;
    font-size: 56px;
    line-height: 58px;
    letter-spacing: 1px;
    text-transform: uppercase;
  }
  .phone {
    position: absolute;
    left: 704px;
    top: 714px;
    color: var(--sky);
    font-weight: 600;
    font-size: 50px;
    line-height: 60px;
  }
</style>
</head>
<body>
  <div class="sticker">
    <svg class="header-shape" viewBox="0 0 1200 901" aria-hidden="true">
      <polygon points="60,60 946,60 1140,254 1140,588 60,588" fill="var(--navy)"/>
      <polygon points="980,62 1140,62 1140,220" fill="var(--sky)"/>
    </svg>
    <h1 class="headline">In case of<br>emergency or<br>for access<br>contact</h1>
    <div class="contact-box"></div>
    <div class="brand">
      <span class="brand-square"></span>
      <span class="brand-name">Harbor<br>Industrial</span>
    </div>
    <p class="phone">(555) 014-2290</p>
  </div>
</body>
</html>
```